Brannock's furniture partial wrap

Needing a partial wrap for this Branno'cks furniture % appliances truck. Wanting something clean and attractive using some of the red thats in the logo. Would want to logo fairly big in the center

Requirements
Must have
• Logo fairly big and visible
Nice to have
• Want the design simple but yet with a professional look with design that flows with the attached logo and colors

```html
<!DOCTYPE html>
<html lang="en">
<head>
<meta charset="UTF-8">
<title>Brannock's Furniture &amp; Appliances – Partial Wrap</title>
<link rel="stylesheet" href="https://fonts.googleapis.com/css2?family=Open+Sans:wght@400;600;700&display=swap">
<style>
  :root {
    --wrap-white: #ffffff;
    --brand-red: #d3000b;
    --brand-black: #0c0c0c;
    --text-black: #111111;
  }
  html, body {
    margin: 0;
    padding: 0;
    width: 1200px;
    height: 542px;
    overflow: hidden;
    background: var(--wrap-white);
  }
  .wrap-panel {
    position: relative;
    width: 1200px;
    height: 542px;
    background: var(--wrap-white);
    font-family: "Open Sans", Arial, sans-serif;
    color: var(--text-black);
  }
  .wrap-shapes {
    position: absolute;
    inset: 0;
  }
  .company-name {
    position: absolute;
    left: 62px;
    top: 168px;
    margin: 0;
    font-size: 74px;
    font-weight: 400;
    letter-spacing: 0.5px;
    line-height: 1;
  }
  .company-tagline {
    position: absolute;
    left: 66px;
    top: 268px;
    margin: 0;
    font-size: 30px;
    font-weight: 400;
    line-height: 1;
  }
  .phone-line {
    position: absolute;
    left: 365px;
    top: 368px;
    display: flex;
    align-items: center;
    gap: 8px;
    color: var(--wrap-white);
    font-size: 22px;
    font-weight: 600;
  }
  .brand-mark {
    position: absolute;
    left: 585px;
    top: 210px;
    display: flex;
    align-items: center;
    gap: 22px;
  }
  .brand-mark-circle {
    width: 128px;
    height: 128px;
    border-radius: 50%;
    border: 14px solid var(--brand-black);
    box-sizing: border-box;
  }
  .brand-mark-name {
    font-size: 64px;
    font-weight: 700;
    color: var(--brand-red);
    line-height: 1;
  }
  .web-line {
    position: absolute;
    left: 780px;
    top: 110px;
    display: flex;
    align-items: center;
    gap: 8px;
    font-size: 22px;
    font-weight: 400;
  }
</style>
</head>
<body>
<main class="wrap-panel">
  <svg class="wrap-shapes" width="1200" height="542" viewBox="0 0 1200 542" aria-hidden="true">
    <polygon class="accent-band-black" points="800,58 1200,36 1200,60 760,104" fill="var(--brand-black)"/>
    <polygon class="accent-band-red" points="60,410 600,340 565,420 60,420" fill="var(--brand-red)"/>
  </svg>

  <h1 class="company-name">BRANNOCK’S</h1>
  <p class="company-tagline">FURNITURE &amp; APPLIANCES</p>

  <div class="phone-line">
    <svg width="22" height="22" viewBox="0 0 24 24" aria-hidden="true">
      <circle cx="12" cy="12" r="11" fill="var(--wrap-white)"/>
      <path d="M8.2 6.5c.4-.4 1-.4 1.3 0l1.3 1.6c.3.4.3.9 0 1.2l-.8.8c.6 1.3 1.6 2.4 2.9 3l.8-.8c.3-.3.9-.4 1.2 0l1.6 1.3c.4.3.4.9 0 1.3l-.9.9c-.7.7-1.8.8-2.7.3-2.3-1.2-4.1-3-5.3-5.3-.5-.9-.4-2 .3-2.7z" fill="var(--brand-red)"/>
    </svg>
    <span>(204) 555-0187</span>
  </div>

  <div class="brand-mark">
    <div class="brand-mark-circle"></div>
    <span class="brand-mark-name">Brannock’s</span>
  </div>

  <div class="web-line">
    <svg width="24" height="24" viewBox="0 0 24 24" aria-hidden="true">
      <circle cx="12" cy="12" r="11" fill="var(--brand-red)"/>
      <g fill="none" stroke="var(--wrap-white)" stroke-width="1.3">
        <circle cx="12" cy="12" r="7"/>
        <ellipse cx="12" cy="12" rx="3" ry="7"/>
        <line x1="5" y1="12" x2="19" y2="12"/>
        <line x1="6" y1="8.5" x2="18" y2="8.5"/>
        <line x1="6" y1="15.5" x2="18" y2="15.5"/>
      </g>
    </svg>
    <span>WWW.BRANNOCKSFURNITURE.NET</span>
  </div>
</main>
</body>
</html>
```